" O projeto zimbo viva é um App para celular no qual o usuário paga uma pequena mensalidade e tem direito a consumir uma bebida por dia nos bares associados. "

```html
<!DOCTYPE html>
<html lang="pt-BR">
<head>
<meta charset="utf-8">
<title>zimbo viva — papel timbrado</title>
<link rel="stylesheet" href="https://fonts.googleapis.com/css2?family=Roboto:wght@300;400;500&display=swap">
<style>
  :root {
    --backdrop: #ecebe8;
    --paper: #ffffff;
    --ink: #1c1c1c;
    --ink-soft: #444444;
    --corner-blue: #5a78c8;
    --deco-pink: #f4c6dc;
    --deco-blue: #c8d6f2;
    --deco-violet: #dcc8f0;
    --icon-grey: #7a7a7a;
  }
  * { box-sizing: border-box; margin: 0; padding: 0; }
  html, body { width: 1200px; height: 1200px; overflow: hidden; }
  body {
    background: var(--backdrop);
    font-family: "Roboto", Arial, sans-serif;
    color: var(--ink);
    position: relative;
  }
  .letterhead {
    position: absolute;
    left: 197px; top: 30px;
    width: 806px; height: 1140px;
    background: var(--paper);
    box-shadow: 0 4px 18px rgba(0,0,0,.18);
    overflow: hidden;
  }
  .corner-accent { position: absolute; left: 0; top: 0; }
  .background-motif {
    position: absolute;
    left: 40px; top: 620px;
    width: 560px; height: 520px;
    background: linear-gradient(135deg, var(--deco-pink) 0%, var(--deco-violet) 50%, var(--deco-blue) 100%);
    opacity: .18;
  }
  .brand {
    position: absolute;
    top: 110px; left: 0; width: 100%;
    display: flex; justify-content: center; align-items: center; gap: 10px;
  }
  .brand-dot {
    width: 14px; height: 14px; border-radius: 50%;
    background: var(--ink);
  }
  .brand-name {
    font-weight: 500; font-size: 34px; letter-spacing: .5px;
    color: var(--ink);
  }
  .content {
    position: absolute;
    left: 78px; top: 232px; width: 660px;
  }
  .title {
    font-weight: 300; font-size: 40px; letter-spacing: 1px;
    margin-bottom: 22px;
  }
  .content p {
    font-size: 13.6px; line-height: 20.5px;
    text-align: justify;
    margin-bottom: 16px;
    color: var(--ink);
  }
  .content p.gap-before { margin-top: 22px; }
  .signature {
    position: absolute; left: 78px; top: 1000px; width: 230px;
  }
  .signature-mark {
    width: 150px; height: 60px; margin-left: 10px;
    background: linear-gradient(90deg, #e8e8e8, #d0d0d0);
    border-radius: 4px;
  }
  .signature-name { font-size: 12px; text-align: right; margin-top: 4px; padding-right: 40px; }
  .signature-role { font-size: 11px; text-align: right; color: var(--ink-soft); padding-right: 40px; }
  .contacts {
    position: absolute; left: 480px; top: 1005px;
    list-style: none;
  }
  .contacts li {
    display: flex; align-items: center; gap: 8px;
    font-size: 10.5px; color: var(--ink-soft);
    height: 27px;
  }
  .contacts svg { flex: none; }
</style>
</head>
<body>
  <main class="letterhead">
    <svg class="corner-accent" width="60" height="60" viewBox="0 0 60 60" aria-hidden="true">
      <polygon points="0,0 60,0 0,60" fill="var(--corner-blue)"/>
    </svg>

    <div class="background-motif" role="img" aria-label="Área do grafismo decorativo suave da marca"></div>

    <header class="brand">
      <span class="brand-dot"></span>
      <span class="brand-name">zimbo viva</span>
    </header>

    <section class="content">
      <h1 class="title">TÍTULO</h1>
      <p>Lorem Ipsum é simplesmente uma simulação de texto da indústria tipográfica e de impressos, e vem sendo utilizado desde o século XVI, quando um impressor desconhecido pegou uma bandeja de tipos e os embaralhou para fazer um livro de modelos de tipos. Lorem Ipsum sobreviveu não só a cinco séculos, como também ao salto para a editoração eletrônica, permanecendo essencialmente inalterado. Se popularizou na década de 60, quando a Letraset lançou decalques contendo passagens de Lorem Ipsum, e mais recentemente quando passou a ser integrado a softwares de editoração eletrônica como Aldus PageMaker.</p>
      <p class="gap-before">Lorem Ipsum é simplesmente uma simulação de texto da indústria tipográfica e de impressos, e vem sendo utilizado desde o século XVI, quando um impressor desconhecido pegou uma bandeja de tipos e os embaralhou para fazer um livro de modelos de tipos. Lorem Ipsum sobreviveu não só a cinco séculos, como também ao salto para a editoração eletrônica, permanecendo essencialmente inalterado. Se popularizou na década de 60, quan</p>
      <p>Lorem Ipsum é simplesmente uma simulação de texto da indústria tipográfica e de impressos, e vem sendo utilizado desde o século XVI, quando um impressor desconhecido pegou uma bandeja de tipos e os embaralhou para fazer</p>
      <p>Lorem Ipsum é simplesmente uma simulação de texto da indústria tipográfica e de impressos, e vem sendo utilizado desde o século XVI, quando um impressor desconhecido pegou uma bandeja de tipos e os embaralhou para fazer</p>
      <p>Lorem Ipsum é simplesmente uma simulação de texto da indústria tipográfica e de impressos, e vem sendo utilizado desde o século XVI, quando um impressor desconhecido pegou uma bandeja de tipos e os embaralhou para fazer</p>
    </section>

    <footer>
      <div class="signature">
        <div class="signature-mark" role="img" aria-label="Espaço da assinatura manuscrita do responsável"></div>
        <div class="signature-name">Nome do Responsável</div>
        <div class="signature-role">Cargo</div>
      </div>

      <ul class="contacts">
        <li>
          <svg width="16" height="16" viewBox="0 0 16 16" aria-hidden="true"><circle cx="8" cy="8" r="7.3" fill="none" stroke="var(--icon-grey)"/><path d="M5.5 4.5l1.5 0 .6 1.8-1 .8a5 5 0 0 0 2.3 2.3l.8-1 1.8.6 0 1.5c-3.5.3-6.3-2.5-6-6z" fill="var(--icon-grey)"/></svg>
          (00) 0000-0000 | (00) 00000-0000
        </li>
        <li>
          <svg width="16" height="16" viewBox="0 0 16 16" aria-hidden="true"><circle cx="8" cy="8" r="7.3" fill="none" stroke="var(--icon-grey)"/><rect x="5.5" y="4" width="5" height="8" rx="1" fill="none" stroke="var(--icon-grey)"/></svg>
          (00) 0000-0000 | (00) 00000-0000
        </li>
        <li>
          <svg width="16" height="16" viewBox="0 0 16 16" aria-hidden="true"><circle cx="8" cy="8" r="7.3" fill="none" stroke="var(--icon-grey)"/><rect x="4.5" y="5.5" width="7" height="5" fill="none" stroke="var(--icon-grey)"/><path d="M4.5 5.5l3.5 3 3.5-3" fill="none" stroke="var(--icon-grey)"/></svg>
          contato@zimboviva.com.br
        </li>
        <li>
          <svg width="16" height="16" viewBox="0 0 16 16" aria-hidden="true"><circle cx="8" cy="8" r="7.3" fill="none" stroke="var(--icon-grey)"/><circle cx="8" cy="8" r="3.5" fill="none" stroke="var(--icon-grey)"/><path d="M4.5 8h7M8 4.5v7" stroke="var(--icon-grey)"/></svg>
          www.zimboviva.com.br
        </li>
      </ul>
    </footer>
  </main>
</body>
</html>
```